チラシは対象のお子様の親に見て頂きます。(1番)
地域の保健師・相談員(このようなサービスを紹介する人)や保育所等の先生にも見られると思います。
こちらで作ったものをアレンジして頂きたいと思います。
全て使用しなくでも大丈夫です。
写真を使用していきたいのですが、いま題材がないので、ネットのサンプル画像を利用して頂けると幸いです。どのような写真があればいいか教えて頂ければ、弊社での撮影も可能です。
A4
片面
• 高解像度JPG (.jpg)
• イラストレーター形式 (.ai)

```html
<!DOCTYPE html>
<html lang="ja">
<head>
<meta charset="utf-8">
<title>保育所等訪問支援のご案内</title>
<link href="https://fonts.googleapis.com/css2?family=M+PLUS+Rounded+1c:wght@400;500;700;800&display=swap" rel="stylesheet">
<style>
:root{
  --paper:#fbfaf3;
  --mint:#8cc9a6;
  --mint-dark:#3f9a6b;
  --mint-pale:#e6f3ea;
  --pink:#ec6f8f;
  --pink-pale:#fbe3ea;
  --ink:#4a4a4a;
  --soft:#7a7a7a;
  --line:#cfe5d7;
}
*{box-sizing:border-box;margin:0;padding:0}
html,body{width:849px;height:1200px;overflow:hidden}
body{background:var(--paper);font-family:"M PLUS Rounded 1c",sans-serif;color:var(--ink);position:relative}
.abs{position:absolute}

.worries{left:0;top:0;width:849px;height:100px}
.bubble{position:absolute;background:#fff;border:2px solid var(--mint);border-radius:50%;display:flex;align-items:center;justify-content:center;text-align:center;font-size:13px;line-height:1.4;color:var(--mint-dark);font-weight:500}
.bubble.pink{border-color:var(--pink);color:var(--pink)}

.lead{top:112px;left:0;width:849px;text-align:center;font-size:19px;font-weight:700;line-height:1.55}
.lead .hl{background:var(--pink);color:#fff;padding:0 4px;border-radius:3px}
.headline{top:172px;left:0;width:849px;text-align:center;font-size:50px;font-weight:800;color:var(--pink);letter-spacing:2px}
.subline{top:238px;left:234px;width:380px;text-align:center;font-size:23px;font-weight:700;color:var(--mint-dark);border-top:2px solid var(--mint);border-bottom:2px solid var(--mint);padding:4px 0}
.intro{top:286px;left:180px;width:490px;text-align:center;font-size:11.5px;line-height:1.7;color:var(--soft)}

.tag{position:absolute;width:62px;height:62px;border-radius:50%;background:var(--mint);color:#fff;font-size:13px;font-weight:700;display:flex;align-items:center;justify-content:center;text-align:center;line-height:1.2}
.tag-text{position:absolute;font-size:12px;line-height:1.65;width:300px}

.photo{position:absolute;border-radius:8px}
.photo-direct{left:430px;top:382px;width:190px;height:150px;background:linear-gradient(135deg,#f4dcc8,#e9c7ae)}
.photo-indirect{left:630px;top:470px;width:190px;height:150px;background:linear-gradient(135deg,#f7ece0,#dcd2c6)}
.note{position:absolute;background:#fff;border:1.5px solid var(--line);border-radius:6px;padding:8px 10px;font-size:11px;line-height:1.6}
.note h4{color:var(--pink);font-size:13px;margin-bottom:3px}

.info{left:40px;top:520px;width:320px}
.info-block{margin-bottom:16px}
.info-block h3{display:inline-block;background:var(--pink);color:#fff;font-size:13px;font-weight:700;padding:2px 14px;border-radius:12px;margin-bottom:6px}
.info-block p{font-size:12px;line-height:1.7}
.info-block small{display:block;font-size:10px;color:var(--soft);line-height:1.5}

.flow{left:390px;top:640px;width:430px}
.flow-title{display:inline-block;background:var(--pink);color:#fff;font-size:18px;font-weight:700;padding:4px 22px;border-radius:18px;margin-bottom:12px}
.steps{display:grid;grid-template-columns:1fr 1fr;gap:12px 14px}
.step{background:#fff;border:1.5px solid var(--mint);border-radius:8px;padding:8px 10px;min-height:128px}
.step h4{font-size:14px;color:var(--mint-dark);margin-bottom:5px;display:flex;align-items:center;gap:6px}
.step h4 .num{width:22px;height:22px;border-radius:50%;background:var(--mint);color:#fff;display:inline-flex;align-items:center;justify-content:center;font-size:12px}
.step p{font-size:10.5px;line-height:1.55}
.step.wide{grid-column:1/3;min-height:44px}

.footer{left:0;top:1030px;width:849px;height:170px;background:#fff;border-top:3px solid var(--mint)}
.footer-ask{position:absolute;left:150px;top:12px;font-size:13px;color:var(--soft)}
.brand{position:absolute;left:150px;top:36px;display:flex;align-items:center;gap:10px;font-size:28px;font-weight:700;color:var(--mint-dark)}
.brand .dot{width:30px;height:30px;border-radius:50%;background:var(--mint)}
.brand-mark{position:absolute;left:40px;top:30px;width:90px;height:90px;border-radius:50%;background:var(--mint-pale)}
.contact{position:absolute;left:150px;top:82px;font-size:12px;line-height:1.6}
.tel{position:absolute;left:150px;top:100px;font-size:34px;font-weight:800;color:var(--ink);display:flex;align-items:center;gap:8px}
.tel small{font-size:16px}
.hours{position:absolute;left:150px;top:146px;font-size:10px;color:var(--soft)}
.map{position:absolute;left:580px;top:14px;width:240px;height:142px;background:#eef0ea;border:1px solid var(--line)}
</style>
</head>
<body>

<div class="abs worries">
  <div class="bubble pink" style="left:20px;top:6px;width:150px;height:78px">お友達と<br>なかなか遊べない</div>
  <div class="bubble" style="left:220px;top:4px;width:170px;height:80px">活動に集中できず、<br>参加が難しい</div>
  <div class="bubble" style="left:440px;top:10px;width:170px;height:70px">行事への参加が難しい</div>
  <div class="bubble pink" style="left:660px;top:4px;width:165px;height:82px">勉強が苦手で<br>ついていけない</div>
</div>

<p class="abs lead">作業療法士が訪問し、<br>お子さんと施設スタッフを<span class="hl">応援</span>します。</p>
<h1 class="abs headline">「保育所等訪問支援」</h1>
<p class="abs subline">サービスをご利用ください</p>
<p class="abs intro">保育所や幼稚園、学校などでの集団生活に困りごとのあるお子さんへ、専門職が訪問して支援を行います。お子さんが過ごす場所で、先生方と一緒に関わり方を考えていく、国の制度に基づくサービスです。</p>

<div class="tag" style="left:40px;top:345px">支援<br>内容</div>
<p class="tag-text" style="left:112px;top:350px">保護者の要望がございましたら、集団生活への適応のための支援をいたします。</p>
<div class="tag" style="left:40px;top:425px">訪問<br>スタッフ</div>
<p class="tag-text" style="left:112px;top:430px">お子さんの支援に必要な知識のある専門職（作業療法士、保育士、児童指導員など）がお伺いいたします。</p>

<div class="photo photo-direct" role="img" aria-label="先生と子どもが一緒に遊ぶ写真"></div>
<div class="photo photo-indirect" role="img" aria-label="子どもが机で勉強している写真"></div>
<div class="note" style="left:630px;top:330px;width:190px">
  <h4>●直接支援</h4>お子さんの集団生活の中で、活動に参加できるよう直接関わり、練習や工夫を一緒に行います。
</div>
<div class="note" style="left:430px;top:540px;width:190px">
  <h4>●間接支援</h4>先生方と関わり方や環境の工夫について話し合い、一緒に考えます。
</div>

<div class="abs info">
  <div class="info-block"><h3>対象</h3><p>保育園、幼稚園、認定こども園、小学校、中学校、特別支援学校、放課後児童クラブ（学童保育）、乳児院などに在籍しているお子さん</p></div>
  <div class="info-block"><h3>頻度</h3><p>原則、月に１〜２回</p><small>※個別に相談に応じます。</small></div>
  <div class="info-block"><h3>利用料</h3><p>多くの場合、費用の１割が自己負担となります。ご家庭の所得により上限がございます。</p><small>※詳しくはお問い合わせください。</small></div>
  <div class="info-block"><h3>情報共有</h3><p>訪問後は、保護者の方と支援の内容や様子を共有し、今後の関わり方を一緒に考えます。</p></div>
</div>

<div class="abs flow">
  <h2 class="flow-title">ご利用の流れ</h2>
  <div class="steps">
    <div class="step"><h4><span class="num">1</span>相談</h4><p>お電話でサービス内容の説明を行い、見学や面談の日程を決めます。まずはお気軽にご相談ください。</p></div>
    <div class="step"><h4><span class="num">2</span>所属先への説明・同意</h4><p>保護者の方から所属先へ訪問のご希望をお伝えいただき、同意を得ます。必要に応じて説明に伺います。</p></div>
    <div class="step"><h4><span class="num">3</span>サービスの申請・手続き</h4><p>お住まいの市町村の窓口で申請を行い、受給者証を受け取ります。</p></div>
    <div class="step"><h4><span class="num">4</span>個別支援計画の作成</h4><p>保護者の方、所属先の先生と話し合い、お子さんに合った支援計画を作ります。</p></div>
    <div class="step wide"><h4><span class="num">5</span>サービスの開始</h4></div>
  </div>
</div>

<footer class="abs footer">
  <div class="brand-mark" role="img" aria-label="事業所の写真"></div>
  <p class="footer-ask">詳しくはお問い合わせください。</p>
  <div class="brand"><span class="dot"></span>こどもデイサービス ひだまり</div>
  <p class="contact">福岡県みどり市さくら町1-2-3　www.hidamari-kids.example</p>
  <div class="tel">
    <svg width="30" height="30" viewBox="0 0 24 24" aria-hidden="true"><path fill="#3f9a6b" d="M6.6 10.8a15 15 0 0 0 6.6 6.6l2.2-2.2a1 1 0 0 1 1-.25 11.4 11.4 0 0 0 3.6.6 1 1 0 0 1 1 1V20a1 1 0 0 1-1 1A17 17 0 0 1 3 4a1 1 0 0 1 1-1h3.5a1 1 0 0 1 1 1 11.4 11.4 0 0 0 .6 3.6 1 1 0 0 1-.25 1z"/></svg>
    <small>TEL.</small>0948-00-1234
  </div>
  <p class="hours">営業時間 9:00〜18:00　定休日 日曜・祝日</p>
  <div class="map" role="img" aria-label="事業所周辺の地図"></div>
</footer>

</body>
</html>
```